Super Stunning and Creative 1-page Infographic Needed

Take the attached content and covert it into a 1-page 8.5x11" stunning, and highly engaging infographic. The infographic must:

* Use Birch Supply colors
* Have icons and graphics used appropriately
* Look unique and creative, and super cool
* Be very eye catching

See attachment for content.

The topic is about retail inventory management. Retail = Store. Not warehouse looking. If you can add Birch Supply photos, this may enhance it. Just a consideration, but not necessary.

Target Market(s)

Birch Supply Store Owners

Industry/Entity Type

Retail Industry - Home Improvement

Font styles to use
Sans Serif

Requirements
Must have
• Birch Supply Colors, Super Creative, Stunning and Eye Capturing. Graphics and icons where they make sense.
Should not have
• Common infographic look. It must look different.

```html
<!DOCTYPE html>
<html lang="en">
<head>
<meta charset="utf-8">
<title>Inventory Management – Birch Supply Store Systems &amp; Operations</title>
<link href="https://fonts.googleapis.com/css2?family=Montserrat:wght@500;600;700;800&family=Open+Sans:wght@400;600&family=Saira+Condensed:wght@700&family=Teko:wght@500&display=swap" rel="stylesheet">
<style>
  :root {
    --red: #e31b2f;
    --blue: #0d4fc4;
    --yellow: #f7e400;
    --ink: #2b2b2b;
    --grey: #5c5c5c;
    --line: #4a4a4a;
    --paper: #ffffff;
  }
  * { box-sizing: border-box; margin: 0; padding: 0; }
  html, body { width: 990px; height: 1200px; overflow: hidden; background: var(--paper); }
  .page {
    position: relative; width: 990px; height: 1200px;
    background: linear-gradient(135deg, #ffffff 0%, #f6f6f6 45%, #ffffff 100%);
    font-family: "Open Sans", sans-serif; color: var(--ink);
  }
  .brand-title { position: absolute; left: 92px; top: 36px; }
  .brand-title .big { font-family: "Montserrat", sans-serif; font-weight: 800; font-size: 31px; color: var(--red); line-height: 1; letter-spacing: -0.5px; }
  .brand-title .small { display: flex; align-items: center; gap: 6px; font-family: "Montserrat", sans-serif; font-weight: 500; font-size: 17px; color: var(--grey); margin-top: 2px; }
  .brand-title .small svg { width: 22px; height: 20px; }
  .dept { position: absolute; left: 412px; top: 58px; display: flex; align-items: center; gap: 14px; }
  .dept .name { font-family: "Montserrat", sans-serif; font-weight: 800; font-size: 32px; color: var(--red); }
  .dept .divider { width: 1.5px; height: 40px; background: #bbb; }
  .dept .unit { font-family: "Montserrat", sans-serif; font-weight: 700; line-height: 1.05; }
  .dept .unit .top { font-size: 14px; color: var(--grey); letter-spacing: 0.5px; }
  .dept .unit .bottom { font-size: 22px; color: var(--red); letter-spacing: 0.5px; }
  .products { position: absolute; left: 730px; top: 22px; width: 165px; height: 108px; border-radius: 8px;
    background: linear-gradient(160deg, #f1f1f1 0%, #d9262f 55%, #2f7fd0 100%); }
  .tip { position: absolute; left: 0; width: 990px; height: 124px; }
  .tip svg { position: absolute; left: 0; top: 0; }
  .tip .num { font-family: "Teko", sans-serif; font-weight: 500; font-size: 36px; color: var(--red); fill: var(--red); }
  .tip h2 { position: absolute; left: 189px; top: 27px; font-family: "Saira Condensed", sans-serif; font-weight: 700;
    font-size: 13.5px; color: var(--blue); letter-spacing: 0.3px; text-transform: uppercase; white-space: nowrap; }
  .tip p { position: absolute; left: 189px; top: 47px; width: 700px; font-size: 11px; line-height: 14.5px; color: var(--ink); }
  .icon { fill: none; stroke: var(--red); stroke-width: 1.8; stroke-linecap: round; stroke-linejoin: round; }
  .more { position: absolute; left: 0; width: 990px; top: 1102px; text-align: center; font-family: "Montserrat", sans-serif; font-weight: 500; font-size: 11.5px; line-height: 18px; color: #111; }
  .contact { position: absolute; left: 58px; top: 1148px; width: 874px; height: 31px; border-radius: 16px; background: #161616; }
  .contact .label { position: absolute; left: 34px; top: 7px; font-family: "Montserrat", sans-serif; font-weight: 700; font-size: 14px; letter-spacing: 1.5px; color: #fff; }
  .contact .details { position: absolute; left: 294px; top: 0; right: 0; height: 31px; border-radius: 16px; background: var(--red);
    display: flex; align-items: center; gap: 52px; padding-left: 22px; font-family: "Montserrat", sans-serif; font-weight: 500; font-size: 15.5px; color: #fff; }
  .contact .details span { display: flex; align-items: center; gap: 8px; }
  .contact svg { width: 16px; height: 16px; fill: none; stroke: #fff; stroke-width: 1.6; }
</style>
</head>
<body>
<div class="page">

  <header>
    <div class="brand-title">
      <div class="big">Inventory</div>
      <div class="small">
        <svg viewBox="0 0 22 20"><rect x="1" y="4" width="11" height="11" fill="none" stroke="#333" stroke-width="1.6"/><line x1="16" y1="2" x2="16" y2="17" stroke="#333" stroke-width="1.6"/><line x1="16" y1="17" x2="21" y2="17" stroke="#333" stroke-width="1.6"/></svg>
        Management
      </div>
    </div>
    <div class="dept">
      <div class="name">BIRCH</div>
      <div class="divider"></div>
      <div class="unit"><div class="top">STORE SYSTEMS &amp;</div><div class="bottom">OPERATIONS</div></div>
    </div>
    <div class="products" role="img" aria-label="Photo of Birch Supply store products: paint bucket, tool bag and tape rolls"></div>
  </header>

  <!-- reusable tip frame -->
  <svg width="0" height="0" style="position:absolute">
    <defs>
      <g id="gauge">
        <path d="M136.5 3.9 A56 56 0 0 0 94 106.5" fill="none" stroke="var(--line)" stroke-width="2"/>
        <circle cx="136.5" cy="3.9" r="2.5" fill="var(--line)"/>
        <circle cx="94" cy="106.5" r="2.5" fill="var(--line)"/>
        <path d="M130 11.7 A47 47 0 0 0 81.3 81.5" fill="none" stroke="var(--red)" stroke-width="9"/>
        <circle cx="122" cy="58" r="42" fill="#fff" stroke="var(--ink)" stroke-width="2"/>
        <circle cx="122" cy="58" r="38" fill="none" stroke="var(--yellow)" stroke-width="7"/>
        <circle cx="122" cy="58" r="34" fill="#fff" stroke="var(--ink)" stroke-width="2"/>
      </g>
      <g id="frame">
        <path d="M248 20 H880 A39 39 0 0 1 880 98 H180" fill="none" stroke="var(--line)" stroke-width="1.6"/>
        <path d="M922 59 A42 42 0 0 1 880 101 H838" fill="none" stroke="var(--blue)" stroke-width="6"/>
      </g>
    </defs>
  </svg>

  <section class="tip" style="top:106px">
    <svg width="990" height="124"><use href="#frame"/><use href="#gauge"/><text class="num" x="189" y="30">01</text>
      <g class="icon" transform="translate(122 58)"><rect x="-14" y="-14" width="12" height="12" stroke-dasharray="2 2"/><rect x="2" y="2" width="12" height="12"/><path d="M4 -12 A8 8 0 0 1 12 -4 M9 -7 L12 -4 L15 -7 M-4 12 A8 8 0 0 1 -12 4 M-15 7 L-12 4 L-9 7"/></g></svg>
    <h2>Getting my replenishment settings right is the most important way to manage inventory</h2>
    <p>Maintaining strong inventory record accuracy (IRA) is the most critical factor toward staying in stock, addressing dead inventory, and driving incremental profitability.</p>
  </section>

  <section class="tip" style="top:230px">
    <svg width="990" height="124"><use href="#frame"/><use href="#gauge"/><text class="num" x="189" y="30">02</text>
      <g class="icon" transform="translate(122 58)"><path d="M-6 4 V-6 M0 2 V-10 M6 0 V-14 M-16 2 L-6 -10 L0 -6 L12 -18 M6 -18 H12 V-12 M-16 14 C-8 8 -2 12 6 8 C10 6 14 4 16 8 C10 14 0 18 -10 18"/></g></svg>
    <h2>When sales have slowed, inventory needs cutting</h2>
    <p>Efforts to reduce inventory can be lethal, creating out of stocks, empty shelves, poor store image perception, and frustrated customers who will ultimately shop the competition. Instead, if inventories need to be reduced, prioritize by looking at unproductive products taking a more strategic approach to healthier inventory levels.</p>
  </section>

  <section class="tip" style="top:354px">
    <svg width="990" height="124"><use href="#frame"/><use href="#gauge"/><text class="num" x="189" y="30">03</text>
      <g class="icon" transform="translate(122 58)"><path d="M-16 -6 L0 -18 L16 -6 V18 H-16 Z"/><rect x="-12" y="-2" width="8" height="8"/><rect x="-2" y="-2" width="8" height="8"/><rect x="-12" y="8" width="8" height="8"/><rect x="-2" y="8" width="8" height="8"/><rect x="8" y="4" width="6" height="12"/><path d="M-20 -18 V-6 M-23 -9 L-20 -6 L-17 -9"/></g></svg>
    <h2>Dead stock (stuff that hasn’t sold in years) needs to be marked down and moved out</h2>
    <p>Leverage markdowns as a last resort. Instead, first check to see if the product is even physically in the store, priced competitively, redundant product in the set, or merchandised effectively. More times than not you can move product without having to sell it at a discount.</p>
  </section>

  <section class="tip" style="top:478px">
    <svg width="990" height="124"><use href="#frame"/><use href="#gauge"/><text class="num" x="189" y="30">04</text>
      <g class="icon" transform="translate(122 58)"><rect x="-8" y="-16" width="22" height="28"/><path d="M-8 -10 L-16 -8 L-10 16 L10 16 M-12 -4 L-20 -2 L-14 18 M-3 -9 H9 M-3 -3 H9 M-3 3 H9 M-3 8 H6"/></g></svg>
    <h2>Working my TALLY count sheets will drive sustainable improvements to IRA</h2>
    <p>used to update and correct counts with no regard toward understanding what caused the issues, then this is a band-aid approach and typically won’t provide much long-term IRA gain. Instead, work count sheets to understand the root of operational gaps and retrain staff as necessary for sustainable improvements.</p>
  </section>

  <section class="tip" style="top:602px">
    <svg width="990" height="124"><use href="#frame"/><use href="#gauge"/><text class="num" x="189" y="30">05</text>
      <g class="icon" transform="translate(122 58)"><rect x="-16" y="2" width="12" height="10"/><rect x="-4" y="2" width="12" height="10"/><rect x="-10" y="-8" width="12" height="10"/><path d="M-20 14 H18"/><rect x="6" y="-18" width="10" height="14"/><path d="M8 -13 H14 M8 -9 H14"/><circle cx="6" cy="-18" r="3"/></g></svg>
    <h2>Increasing my inventory depth will hurt profits and drive down my inventory turns</h2>
    <p>Stores who have deeper levels of inventory outperform stores that don’t. When focused on raising inventory strategically through programs like economic order quantities, minimum order points, and preseason planner, inventory turns typically remain the same as inventory increases.</p>
  </section>

  <section class="tip" style="top:726px">
    <svg width="990" height="124"><use href="#frame"/><use href="#gauge"/><text class="num" x="189" y="30">06</text>
      <g class="icon" transform="translate(122 58)"><circle cx="0" cy="3" r="16"/><path d="M-4 -17 H4 M0 -17 V-13 M12 -11 L15 -14"/></g>
      <text x="122" y="67" text-anchor="middle" font-family="Montserrat, sans-serif" font-weight="700" font-size="16" fill="var(--red)">1h</text></svg>
    <h2>Spending more than an hour (or more) working the ‘RSO’ will result in better quality suggested orders</h2>
    <p>Typically, if it takes greater than 60 minutes to work your RSO each week per store, there are larger issues at play. The goal is to be able to review the RSO on an exception basis for outliers and transmit it through to then shift focus on other important store activities.</p>
  </section>

  <section class="tip" style="top:850px">
    <svg width="990" height="124"><use href="#frame"/><use href="#gauge"/><text class="num" x="189" y="30">07</text>
      <g class="icon" transform="translate(122 58)"><path d="M-6 -14 A16 16 0 1 1 -6 14"/><circle cx="4" cy="0" r="2"/><path d="M4 0 L10 -8 M-20 -6 H-8 M-22 0 H-6 M-20 6 H-8"/></g></svg>
    <h2>Carry more weeks of supply on fast moving products and less on slower velocity SKUs</h2>
    <p>Based on how Keystone for Windows calculates order points, this can result in overstocking on faster goods and insufficient amounts of slower ones. Revisit your weeks of supply settings to ensure they are maintained at or near Birch best practice levels.</p>
  </section>

  <section class="tip" style="top:974px">
    <svg width="990" height="124"><use href="#frame"/><use href="#gauge"/><text class="num" x="189" y="30">08</text>
      <g class="icon" transform="translate(122 58)"><circle cx="0" cy="0" r="5"/><path d="M-14 -10 A17 17 0 0 1 10 -14 M16 6 A17 17 0 0 1 4 17"/><rect x="-4" y="-22" width="10" height="7"/><circle cx="-14" cy="10" r="4"/><path d="M-11 13 L-7 17"/><rect x="10" y="12" width="7" height="6"/></g></svg>
    <h2>With the onset of global supply chain issues, reaching a 95% in-stock position is next to impossible</h2>
    <p>Undoubtably, the industry supply problems make obtaining a higher in-stock position more challenging, but still quite probable. The key is to focus on what you are able to control within the four walls of your operations and consistently execute the basics (i.e. count sheets, shooting the outs, item change management).</p>
  </section>

  <footer>
    <div class="more">See the Birch Way of Retailing Inventory Management section for further insights and practices to optimize inventory health.<br>Pathway:&nbsp; BIRCHNET &gt;&gt; About Birch &gt;&gt; Birch Way of Retailing &gt;&gt; Inventory Management</div>
    <div class="contact">
      <div class="label">CONTACT INFORMATION:</div>
      <div class="details">
        <span><svg viewBox="0 0 16 16"><rect x="1.5" y="3.5" width="13" height="9"/><path d="M1.5 3.5 L8 9 L14.5 3.5"/></svg>storeops@birchsupply.example</span>
        <span><svg viewBox="0 0 16 16"><circle cx="8" cy="8" r="6.5"/><path d="M5.5 5 C5.5 8 8 10.5 11 10.5 L11 9 L9.5 8.5 L8.8 9.2 C7.8 8.7 7.3 8.2 6.8 7.2 L7.5 6.5 L7 5 Z"/></svg>555.014.2290</span>
      </div>
    </div>
  </footer>

</div>
</body>
</html>
```